Business Card Design Project

Crestline Vein Center

Dr Tomas Venrick M.D, F.R.C.S
Vascular and Vein Surgery

47-18 Pellham Avenue, Suite 314
Astoria
NY 11287

212-555-0147
718-555-0193
www.crestlinecare.us back of the card for scheduled appointments up to 5 appointment dates

Target Market(s)

Male and Female patients from 25 onwards with spider veins or varicose veins

Industry/Entity Type

Business

Font styles to use
Serif

Colors
86cae6
85abd2
0456a4

Requirements
Must have
• Modern Sophisticated design using light blue and grey text
Should not have
• hearts or flowers

```html
<!DOCTYPE html>
<html lang="en">
<head>
<meta charset="utf-8">
<title>Crestline Vein Center – Business Cards</title>
<link rel="stylesheet" href="https://fonts.googleapis.com/css2?family=Crimson+Pro:wght@400;600&display=swap">
<style>
  :root {
    --brand-blue: #0456a4;
    --brand-blue-deep: #044a8f;
    --mid-blue: #85abd2;
    --light-blue: #86cae6;
    --grey-text: #4a4a4a;
    --card-white: #ffffff;
    --backdrop: #e9ecef;
    --line-dot: #9aa3ad;
  }
  * { box-sizing: border-box; margin: 0; padding: 0; }
  html, body { width: 1200px; height: 1023px; overflow: hidden; }
  body {
    background: var(--backdrop);
    font-family: "Crimson Pro", serif;
    display: flex;
    flex-direction: column;
    align-items: center;
    justify-content: center;
    gap: 56px;
  }
  .card {
    width: 720px;
    height: 412px;
    display: flex;
    background: var(--card-white);
    box-shadow: 0 6px 18px rgba(0,0,0,0.18);
    overflow: hidden;
  }
  .panel-blue {
    background: linear-gradient(160deg, #0a63b3 0%, var(--brand-blue) 55%, var(--brand-blue-deep) 100%);
    color: #fff;
  }

  /* Appointment side */
  .card-back .panel-blue {
    width: 37%;
    display: flex;
    flex-direction: column;
    justify-content: center;
    align-items: center;
    text-align: center;
    font-size: 19px;
    line-height: 1.3;
    gap: 26px;
  }
  .card-back .appointment-side {
    position: relative;
    flex: 1;
    padding: 30px 40px 0 44px;
  }
  .photo-wash {
    position: absolute;
    inset: 0;
    background: radial-gradient(ellipse at 60% 55%, #e7e1dc 0%, #f1eeeb 45%, #f7f7f8 80%);
  }
  .appointment-side > *:not(.photo-wash) { position: relative; }
  .brand-name {
    display: flex;
    align-items: center;
    gap: 10px;
    color: var(--brand-blue);
    font-size: 26px;
    font-weight: 600;
    white-space: nowrap;
  }
  .brand-dot {
    width: 14px; height: 14px;
    border-radius: 50%;
    background: var(--light-blue);
    flex: none;
  }
  .card-back .brand-name { justify-content: center; margin-top: 10px; }
  .appointment-title {
    text-align: center;
    color: var(--grey-text);
    font-size: 20px;
    margin: 22px 0 14px;
  }
  .slot {
    display: flex;
    align-items: baseline;
    gap: 6px;
    color: var(--grey-text);
    font-size: 17px;
    height: 36px;
  }
  .slot .fill {
    flex: 1;
    border-bottom: 1px dotted var(--line-dot);
  }
  .slot .time-label { margin-left: 8px; }

  /* Contact side */
  .card-front .identity-side {
    width: 44%;
    display: flex;
    flex-direction: column;
    align-items: center;
    justify-content: center;
    text-align: center;
    gap: 26px;
  }
  .card-front .brand-name { font-size: 28px; }
  .address {
    color: var(--grey-text);
    font-size: 19px;
    line-height: 1.25;
  }
  .card-front .panel-blue {
    flex: 1;
    padding: 0 40px 0 64px;
    display: flex;
    flex-direction: column;
    justify-content: center;
  }
  .doctor-name { font-size: 25px; font-weight: 600; }
  .specialty { font-size: 18px; margin: 2px 0 30px 30px; }
  .contact-list { list-style: none; font-size: 19px; margin-left: 34px; }
  .contact-list li { display: flex; align-items: center; gap: 12px; height: 25px; }
  .contact-list svg { width: 13px; height: 13px; flex: none; }
</style>
</head>
<body>

  <section class="card card-back" aria-label="Appointment side">
    <div class="panel-blue">
      <p class="back-address">47-18 Pellham Avenue, Suite 314<br>Astoria, NY 11287</p>
      <p class="opening-hours">Opening hours<br>Monday to Saturday<br>9:00am to 5:00pm</p>
    </div>
    <div class="appointment-side">
      <div class="photo-wash" role="img" aria-label="Soft faded photograph of hands caring for a leg"></div>
      <div class="brand-name"><span class="brand-dot"></span>Crestline Vein Center</div>
      <h2 class="appointment-title">Appointment</h2>
      <div class="slot"><span>Date</span><span class="fill"></span><span class="time-label">Time</span><span class="fill"></span></div>
      <div class="slot"><span>Date</span><span class="fill"></span><span class="time-label">Time</span><span class="fill"></span></div>
      <div class="slot"><span>Date</span><span class="fill"></span><span class="time-label">Time</span><span class="fill"></span></div>
      <div class="slot"><span>Date</span><span class="fill"></span><span class="time-label">Time</span><span class="fill"></span></div>
      <div class="slot"><span>Date</span><span class="fill"></span><span class="time-label">Time</span><span class="fill"></span></div>
    </div>
  </section>

  <section class="card card-front" aria-label="Contact side">
    <div class="identity-side">
      <div class="brand-name"><span class="brand-dot"></span>Crestline Vein Center</div>
      <p class="address">47-18 Pellham Avenue, Suite 314,<br>Astoria NY 11287</p>
    </div>
    <div class="panel-blue">
      <h1 class="doctor-name">Dr Tomas Venrick M.D, F.R.C.S</h1>
      <p class="specialty">Vascular and Vein Surgery</p>
      <ul class="contact-list">
        <li>
          <svg viewBox="0 0 16 16" aria-hidden="true"><path fill="#fff" d="M1 6c0-2 3-4 7-4s7 2 7 4v1h-4V5.5H5V7H1zM3 8h10l1 6H2z"/></svg>
          212-555-0147
        </li>
        <li>
          <svg viewBox="0 0 16 16" aria-hidden="true"><rect x="4" y="1" width="8" height="14" rx="1.5" fill="none" stroke="#fff" stroke-width="1.5"/><circle cx="8" cy="12.5" r="0.9" fill="#fff"/></svg>
          718-555-0193
        </li>
        <li>
          <svg viewBox="0 0 16 16" aria-hidden="true"><g fill="none" stroke="#fff" stroke-width="1.2"><circle cx="8" cy="8" r="6.5"/><ellipse cx="8" cy="8" rx="3" ry="6.5"/><path d="M1.5 8h13"/></g></svg>
          www.crestlinecare.us
        </li>
      </ul>
    </div>
  </section>

</body>
</html>
```